Business Card for New Business

Please design a business card using our logo and font files. This is only one card for one person, as listed in details section.

Industry/Entity Type

Business

Contact Information for Business Card

Carl Voserby

Phone 240.318.6624
Cell 703.581.4096
Email carl@moltravex.com

www.moltravex.com

Address
18250 Brennick Lane #314
Damascus, MD 20715

Font styles to use
Sans Serif

Requirements
Must have
• Information listed in detail section. Must be standard card size.

```html
<!DOCTYPE html>
<html lang="en">
<head>
<meta charset="utf-8">
<title>Moltravex Productions – Business Card</title>
<link rel="stylesheet" href="https://fonts.googleapis.com/css2?family=Questrial&display=swap">
<style>
  :root {
    --orange: #c9582b;
    --red: #b8262b;
    --ink: #2b2b2b;
    --grey: #6e6e6e;
    --paper: #ffffff;
    --backdrop: #ececec;
    --font: "Questrial", "Century Gothic", sans-serif;
  }
  * { box-sizing: border-box; margin: 0; padding: 0; }
  html, body { width: 1200px; height: 1200px; overflow: hidden; }
  body { background: var(--backdrop); font-family: var(--font); position: relative; }

  .card {
    position: absolute; left: 170px; width: 860px; height: 536px;
    background: var(--paper); overflow: hidden;
    box-shadow: 0 10px 28px rgba(0,0,0,.18);
  }
  .card--front { top: 42px; }
  .card--back  { top: 622px; }
  .card__art { position: absolute; inset: 0; width: 100%; height: 100%; }

  /* shared brand name placeholder */
  .wordmark { position: absolute; display: flex; align-items: center; gap: 10px; color: var(--ink); white-space: nowrap; }
  .wordmark__dot { width: 16px; height: 16px; border-radius: 50%; background: var(--red); flex: none; }
  .wordmark__name { font-size: 25px; line-height: 1; }

  /* front */
  .card--front .wordmark { left: 52px; top: 250px; }

  .holder { position: absolute; left: 458px; top: 80px; font-size: 38px; font-weight: 400; color: var(--ink); letter-spacing: .5px; }

  .contact { position: absolute; left: 474px; list-style: none; color: var(--grey); font-size: 22px; }
  .contact li { display: flex; align-items: center; gap: 14px; height: 40px; }
  .contact svg { width: 26px; height: 26px; flex: none; }
  .contact--lines { top: 196px; }
  .contact--address { top: 430px; }
  .contact--address li { align-items: flex-start; height: auto; line-height: 38px; }
  .contact--address svg { margin-top: 6px; }

  .website {
    position: absolute; left: 18px; top: 488px; width: 382px;
    display: flex; align-items: center; gap: 12px;
    color: var(--paper); font-size: 25px; letter-spacing: .5px;
  }
  .website::before, .website::after { content: ""; flex: 1; height: 2px; background: var(--paper); }

  /* back */
  .card--back .band { position: absolute; left: 0; right: 0; top: 172px; bottom: 0; background: var(--orange); }
  .card--back .emblem-area { position: absolute; inset: 0; width: 100%; height: 100%; }
  .card--back .wordmark { left: 50%; top: 60px; transform: translateX(-50%); gap: 18px; }
  .card--back .wordmark__dot { width: 36px; height: 36px; }
  .card--back .wordmark__name { font-size: 56px; }
</style>
</head>
<body>

<section class="card card--front" aria-label="Business card front">
  <svg class="card__art" viewBox="0 0 860 536" aria-hidden="true">
    <rect width="860" height="536" fill="var(--orange)"/>
    <polygon points="481,0 860,0 860,536 481,536 252,263" fill="var(--paper)"/>
    <path d="M52,87 Q30,87 30,112 L30,410 Q30,435 52,435 L360,276 Q378,263 360,250 Z"
          fill="var(--paper)" stroke="var(--red)" stroke-width="5"/>
  </svg>

  <div class="wordmark">
    <span class="wordmark__dot"></span>
    <span class="wordmark__name">Moltravex Productions</span>
  </div>

  <h1 class="holder">Carl Voserby</h1>

  <ul class="contact contact--lines">
    <li>
      <svg viewBox="0 0 26 26"><circle cx="13" cy="13" r="12" fill="var(--red)"/><path d="M9 7c1 0 2 2 2 3s-1 1-1 2 2 4 4 4 1-1 2-1 3 1 3 2-1 2-3 2c-4 0-9-5-9-9 0-2 1-3 2-3z" fill="#fff"/></svg>
      <span>Phone 240.318.6624</span>
    </li>
    <li>
      <svg viewBox="0 0 26 26"><rect x="7" y="2" width="12" height="22" rx="2" fill="none" stroke="var(--red)" stroke-width="2.4"/><circle cx="13" cy="20" r="1.4" fill="var(--red)"/></svg>
      <span>Cell 703.581.4096</span>
    </li>
    <li>
      <svg viewBox="0 0 26 26"><rect x="2" y="6" width="22" height="15" fill="var(--red)"/><path d="M2 6l11 9 11-9" fill="none" stroke="#fff" stroke-width="2"/></svg>
      <span>Email carl@moltravex.com</span>
    </li>
  </ul>

  <ul class="contact contact--address">
    <li>
      <svg viewBox="0 0 26 26"><path d="M13 25s-9-9-9-15a9 9 0 0 1 18 0c0 6-9 15-9 15z" fill="var(--red)"/><circle cx="13" cy="10" r="3.5" fill="#fff"/></svg>
      <span>18250 Brennick Lane<br>#314 Damascus, MD 20715</span>
    </li>
  </ul>

  <p class="website">www.moltravex.com</p>
</section>

<section class="card card--back" aria-label="Business card back">
  <div class="band"></div>
  <svg class="emblem-area" viewBox="0 0 860 536" role="img" aria-label="Large faint brand emblem area">
    <circle cx="424" cy="240" r="260" fill="#ffffff" fill-opacity="0.16" stroke="#ffffff" stroke-opacity="0.25" stroke-width="4"/>
  </svg>
  <div class="wordmark">
    <span class="wordmark__dot"></span>
    <span class="wordmark__name">Moltravex Productions</span>
  </div>
</section>

</body>
</html>
```